Pet Shop Website

website will need to have the following features:
• Photo Galleries of each species (Dogs, Cats, Birds, Fish, Reptiles, Rabbits) in a light box popup
o Each species may have several different categories for example:
 Fish
• Marine fish
• Fresh water
• tropical
• Cichlid
• Information Fact sheets of each species – Downloaded as a pdf which can be either
o Care Sheets
o Training Sheets
• Members Area
o Username (Email Address) & Password login
o New signups
o Exclusive Member Deals
o Newsletter options

The front page must be very simple (for example lumavale.com.au) contain the following:
• Product of the week - which can be purchased online
o Short details
o Cost
• Pet Club Sign up picture
• Animal of the week/month
• Contact Phone Number and addresses of the stores
• A jQuery slideshow (Images could include stores, pets etc…)
The main page MUST keep simple. We do not want it cluttered.

Inner Page
The animals / reptile page will need to have:
• Short description of the species
• Photo Galleries
• A list of what is in stock and the list needs to clearly be sorted by each store (Use of Tabs maybe).
• Facts sheets / Info sheets
The type of website ideas (not the type of look that we are necessary after) is and the sort of content that we want to offer are as follows:

http://www.scalenook.com.au/
http://www.marrowdenpets.com.au/
http://www.thefurloft.com.au
http://www.critterhaven.net.au

Colour in the new website:
Blue
Red
Grey
Yellow

Original site:

http://www.pawglint.com.au
Updates

Hi Guys,

We had feedback from the client and they would like to see a few dark designs.

Thanks                                   

Reason: We would like to reopen this contest back up for a further week

Target Market(s)

Targeting animal lovers

Industry/Entity Type

Store

Requirements
Should not have
• Alter the logo in anyway

```html
<!DOCTYPE html>
<html lang="en">
<head>
<meta charset="utf-8">
<title>Pawglint — Pet Shop</title>
<link rel="stylesheet" href="https://fonts.googleapis.com/css2?family=Arimo:wght@400;700&family=Pathway+Gothic+One&family=Oswald:wght@500&family=Lora:ital@1&display=swap">
<style>
:root{
  --page:#ececec;
  --band:#4ba7c9;
  --band-dark:#3a93b6;
  --badge:#d8ecf6;
  --badge-line:#3c9cc6;
  --heading-blue:#2a8fbd;
  --orange:#d49b12;
  --red:#c41e1e;
  --text:#666;
  --dark:#333;
  --red-tile:#c40f0f;
  --teal-tile:#13a4ae;
  --orange-tile:#de6a3c;
  --blue-tile:#1289bd;
  --yellow-tile:#efc30a;
  --green-tile:#4e8d0b;
  --gold:#f0c021;
  --gold-dark:#d69e0a;
  --footer:#f2f2f2;
}
*{margin:0;padding:0;box-sizing:border-box}
html,body{width:928px;height:1200px;overflow:hidden;background:var(--page)}
body{font-family:"Arimo",Arial,sans-serif;color:var(--text);position:relative}
.abs{position:absolute}
.nav-band{left:0;top:73px;width:928px;height:47px;background:linear-gradient(var(--band),var(--band-dark));border-bottom:2px solid #7fc2dc}
.nav{left:0;top:92px;font-size:11px;color:#fff;display:flex}
.nav a{color:#fff;text-decoration:none;position:absolute;white-space:nowrap}
.nav a.current{text-decoration:underline}
.badge{left:344px;top:36px;width:254px;height:114px}
.brand{left:344px;top:73px;width:254px;text-align:center;font-family:"Pathway Gothic One",sans-serif;font-size:30px;color:var(--red);letter-spacing:1px}
.search{left:695px;top:77px;width:205px;height:36px;border-radius:7px;background:linear-gradient(#f8cf4a,#eeab16);padding:5px}
.search-field{width:171px;height:26px;border-radius:5px;background:#fff;font-size:10px;color:#999;padding:7px 9px}
.search svg{position:absolute;right:8px;top:9px}
.tiles{left:28px;top:157px;width:872px;height:417px}
.tile{position:absolute;width:146px;display:flex;align-items:center;justify-content:center;font-family:"Pathway Gothic One",sans-serif;color:#fff;font-size:40px}
.photo{position:absolute;width:146px}
.notch{position:absolute;left:57px;width:32px;height:16px}
.section-title{font-family:"Pathway Gothic One",sans-serif;font-size:22px;color:var(--heading-blue)}
.framed{border:2px solid var(--badge-line);box-shadow:0 1px 3px rgba(0,0,0,.35)}
.body-text{font-size:11.5px;line-height:15px;letter-spacing:.4px;text-align:justify}
.btn{height:24px;border-radius:3px;background:linear-gradient(#4aa3d6,#1e6da6);border:1px solid #17598a;color:#fff;font-family:"Lora",serif;font-style:italic;font-size:11px;display:flex;align-items:center;justify-content:center;gap:6px}
.signup{left:600px;top:625px;width:301px;height:287px;border:1px solid #d4d4d4;border-radius:8px;background:#f8f8f8;overflow:hidden}
.signup h2{position:absolute;left:96px;top:13px;font-family:"Lora",serif;font-style:italic;font-weight:400;font-size:26px;color:#555}
.label{position:absolute;font-size:11px;color:#555}
.field{position:absolute;left:44px;width:214px;height:36px;border:1px solid #bbb;border-radius:3px;background:linear-gradient(#e4e4e4,#d2d2d2);font-size:11px;color:#666;padding:10px 15px}
.signup-foot{position:absolute;left:0;bottom:0;width:100%;height:66px;background:linear-gradient(var(--gold),var(--gold-dark));font-size:10px;color:#fff}
.signup-foot a{color:var(--red);text-decoration:underline}
.login{position:absolute;left:182px;top:18px;width:80px;height:28px;border-radius:5px;background:linear-gradient(#555,#1a1a1a);color:#fff;font-family:"Oswald",sans-serif;font-size:12px;letter-spacing:1px;display:flex;align-items:center;justify-content:center}
.footer{left:28px;top:949px;width:872px;height:224px;background:var(--footer)}
.footer h3{font-family:"Oswald",sans-serif;font-weight:500;font-size:24px;color:#222;letter-spacing:-.5px}
.social{display:flex;gap:10px;margin-top:10px}
.social span{width:20px;height:20px;border-radius:3px}
.links{list-style:none;font-size:12px;color:#555;line-height:22px}
.links li::before{content:"» ";color:#555}
.loc{font-size:12px;color:#666;line-height:15px}
.loc b{font-weight:400;color:#1a8fd0}
.vline{width:1px;height:110px;background:#ddd}
.rule{left:40px;top:1127px;width:814px;height:5px;background:#000}
.copy{left:40px;top:1147px;font-size:12px;color:#444}
.top-btn{left:854px;top:1073px;width:38px;height:38px;border-radius:50%;background:#fff;border:1px solid #ccc;font-family:"Oswald",sans-serif;font-size:12px;color:#333;display:flex;align-items:center;justify-content:center}
</style>
</head>
<body>

<div class="abs nav-band"></div>
<nav class="abs nav">
  <a class="current" style="left:27px">Home</a>
  <a style="left:84px">About Us</a>
  <a style="left:155px">Pets</a>
  <a style="left:206px">Photogallery</a>
  <a style="left:290px">Contact Us</a>
</nav>

<svg class="abs badge" viewBox="0 0 254 114" aria-hidden="true">
  <path d="M127 4 C120 10 110 12 90 12 H24 C8 12 2 30 2 57 C2 84 8 102 24 102 H90 C110 102 120 104 127 110 C134 104 144 102 164 102 H230 C246 102 252 84 252 57 C252 30 246 12 230 12 H164 C144 12 134 10 127 4 Z" fill="var(--badge)" stroke="var(--badge-line)" stroke-width="3"/>
</svg>
<div class="abs brand">Pawglint</div>

<div class="abs search">
  <div class="search-field">SEARCH</div>
  <svg width="16" height="16" viewBox="0 0 16 16"><circle cx="6.5" cy="6.5" r="4.5" fill="none" stroke="#fff" stroke-width="2"/><line x1="10" y1="10" x2="14.5" y2="14.5" stroke="#fff" stroke-width="2.5" stroke-linecap="round"/></svg>
</div>

<section class="abs tiles">
  <div class="photo" role="img" aria-label="Golden retriever dog" style="left:0;top:0;height:278px;background:linear-gradient(#5b6a30,#b8853c 50%,#8a5e2a)"></div>
  <div class="tile" style="left:0;top:278px;height:139px;background:var(--blue-tile)">DOG</div>

  <div class="tile" style="left:146px;top:0;height:139px;background:var(--red-tile)">CAT</div>
  <div class="photo" role="img" aria-label="White kitten" style="left:146px;top:139px;height:278px;background:linear-gradient(#8a6a48,#e6e2de 40%,#a97c4c)"></div>

  <div class="photo" role="img" aria-label="Clownfish" style="left:292px;top:0;height:278px;background:linear-gradient(#4b3a2c,#c66a2a 45%,#3a2a20)"></div>
  <div class="tile" style="left:292px;top:278px;height:139px;background:var(--yellow-tile)">FISH</div>

  <div class="tile" style="left:438px;top:0;height:139px;background:var(--teal-tile)">BIRDS</div>
  <div class="photo" role="img" aria-label="Budgies on a branch" style="left:438px;top:139px;height:278px;background:linear-gradient(#7a8a5a,#8fbe5a 45%,#6c7a4c)"></div>

  <div class="photo" role="img" aria-label="Green lizard" style="left:584px;top:0;height:278px;background:linear-gradient(#f4f4f0,#8a9a5a 50%,#f2f2ee)"></div>
  <div class="tile" style="left:584px;top:278px;height:139px;background:var(--green-tile)">REPTILES</div>

  <div class="tile" style="left:730px;top:0;height:139px;width:142px;background:var(--orange-tile)">RABBITS</div>
  <div class="photo" role="img" aria-label="Lop-eared rabbit" style="left:730px;top:139px;width:142px;height:278px;background:linear-gradient(#f6ddf2,#e2c6a8 50%,#f6f2ee)"></div>

  <svg class="notch" style="left:203px;top:139px" viewBox="0 0 32 16"><path d="M0 0 A16 16 0 0 0 32 0Z" fill="var(--red-tile)"/><path d="M13 5l3 3 3-3" stroke="#fff" fill="none" stroke-width="1.5"/></svg>
  <svg class="notch" style="left:495px;top:139px" viewBox="0 0 32 16"><path d="M0 0 A16 16 0 0 0 32 0Z" fill="var(--teal-tile)"/><path d="M13 5l3 3 3-3" stroke="#fff" fill="none" stroke-width="1.5"/></svg>
  <svg class="notch" style="left:785px;top:139px" viewBox="0 0 32 16"><path d="M0 0 A16 16 0 0 0 32 0Z" fill="var(--orange-tile)"/><path d="M13 5l3 3 3-3" stroke="#fff" fill="none" stroke-width="1.5"/></svg>
  <svg class="notch" style="left:57px;top:262px" viewBox="0 0 32 16"><path d="M0 16 A16 16 0 0 1 32 16Z" fill="var(--blue-tile)"/><path d="M13 11l3-3 3 3" stroke="#fff" fill="none" stroke-width="1.5"/></svg>
  <svg class="notch" style="left:349px;top:262px" viewBox="0 0 32 16"><path d="M0 16 A16 16 0 0 1 32 16Z" fill="var(--yellow-tile)"/><path d="M13 11l3-3 3 3" stroke="#fff" fill="none" stroke-width="1.5"/></svg>
  <svg class="notch" style="left:641px;top:262px" viewBox="0 0 32 16"><path d="M0 16 A16 16 0 0 1 32 16Z" fill="var(--green-tile)"/><path d="M13 11l3-3 3 3" stroke="#fff" fill="none" stroke-width="1.5"/></svg>
</section>

<!-- product of the week -->
<h2 class="abs section-title" style="left:29px;top:588px">Product of the Week</h2>
<div class="abs framed" role="img" aria-label="Golden retriever puppy on grass" style="left:29px;top:625px;width:227px;height:145px;background:linear-gradient(135deg,#5d8a3a,#e0b67a 50%,#4d7a2e)"></div>
<div class="abs" style="left:28px;top:785px;font-family:'Pathway Gothic One',sans-serif;font-size:21px;color:var(--orange)">Online Purchased</div>
<p class="abs body-text" style="left:31px;top:813px;width:228px">Lorem ipsum dolor sit amet, consectetur adipiscing elit. Cras bibendum ligula id nunc blandit ultricies.</p>
<div class="abs" style="left:31px;top:862px;font-family:'Pathway Gothic One',sans-serif;font-size:21px;color:var(--red)">Price - $45</div>
<div class="abs btn" style="left:169px;top:865px;width:92px">
  <svg width="14" height="14" viewBox="0 0 14 14"><circle cx="7" cy="7" r="6.5" fill="#fff"/><path d="M5.5 4l3 3-3 3" stroke="#1e6da6" stroke-width="1.8" fill="none"/></svg>Add to Cart</div>

<!-- animal of the month -->
<h2 class="abs section-title" style="left:319px;top:588px">Animal of the Month</h2>
<div class="abs framed" role="img" aria-label="Two lop-eared bunnies in a blanket" style="left:318px;top:625px;width:232px;height:145px;background:linear-gradient(135deg,#c8d8ea,#c89460 50%,#dfe8f2)"></div>
<p class="abs body-text" style="left:316px;top:794px;width:229px">Lorem ipsum dolor sit amet, consectetur adipiscing elit. Cras bibendum ligula id nunc blandit ultricies.Lorem ipsum dolor sit amet, consectetur adipiscing elit.</p>
<div class="abs btn" style="left:468px;top:863px;width:83px">More Details</div>

<!-- sign up -->
<section class="abs signup">
  <svg style="position:absolute;left:34px;top:10px" width="52" height="58" viewBox="0 0 52 58" aria-hidden="true">
    <circle cx="16" cy="15" r="11" fill="none" stroke="#999" stroke-width="5"/>
    <rect x="22" y="20" width="6" height="32" rx="2" fill="#b0b0b0" transform="rotate(-20 25 36)"/>
    <circle cx="30" cy="16" r="10" fill="none" stroke="#c9a33a" stroke-width="5"/>
    <rect x="32" y="22" width="6" height="30" rx="2" fill="#d8b64a" transform="rotate(10 35 37)"/>
  </svg>
  <h2>Pet Club Sign up</h2>
  <div class="label" style="left:46px;top:78px">USER NAME</div>
  <div class="field" style="top:95px">username</div>
  <div class="label" style="left:46px;top:148px">PASSWORD</div>
  <div class="field" style="top:162px">*********************</div>
  <svg style="position:absolute;left:50px;top:205px" width="16" height="14" viewBox="0 0 16 14"><path d="M2 7l4 4 8-10" stroke="#4e9a1a" stroke-width="3" fill="none"/></svg>
  <div class="label" style="left:70px;top:209px;font-size:10px">Remember me</div>
  <div class="signup-foot">
    <div style="position:absolute;left:46px;top:19px"><a>learn More</a>&nbsp; information</div>
    <div style="position:absolute;left:46px;top:37px"><a>Register</a>&nbsp; free account</div>
    <div class="login">LOGIN</div>
  </div>
</section>

<!-- footer -->
<footer class="abs footer">
  <div class="abs" style="left:12px;top:51px">
    <h3>Find Us On Social Network</h3>
    <div class="social"><span style="background:#5ec0ea"></span><span style="background:#3b5a9a"></span><span style="background:#d24a3a"></span><span style="background:#333"></span></div>
  </div>
  <div class="abs vline" style="left:318px;top:30px"></div>
  <svg class="abs" style="left:325px;top:51px" width="35" height="35" viewBox="0 0 35 35" aria-hidden="true"><rect width="35" height="35" rx="6" fill="#111"/><text x="17.5" y="28" text-anchor="middle" font-family="Arimo,Arial,sans-serif" font-weight="700" font-size="28" fill="#fff">?</text></svg>
  <ul class="abs links" style="left:377px;top:49px">
    <li>Atcurs usuctunas astique</li>
    <li>Ulsphareec accumsan kertrertase</li>
    <li>Malenec sit ametem ipsumer</li>
    <li>Dolor sit acon sectetus</li>
  </ul>
  <div class="abs vline" style="left:600px;top:30px"></div>
  <div class="abs" style="left:636px;top:47px">
    <h3>Locations</h3>
    <p class="loc" style="margin-top:8px">Unit 4 / 22 Harbourline Drive<br>CORAL BAY, W.A 6701</p>
    <p class="loc" style="margin-top:15px"><b>Phone:</b> (08) 5550 2147<br><b>Fax:</b> (08) 5550 2148</p>
  </div>
</footer>
<div class="abs top-btn">top</div>
<div class="abs rule"></div>
<div class="abs copy">Pawglint (c) 2013-2014 . Privacy Policy</div>

</body>
</html>
```